Complete Website Redesign

We need a complete revamp of our website. Need to add interactive custmer catalog seection tools. Need to add customer spec input for recommended product search results. Need a cutomer lead and opportunity contact capability. Need a complete Branding message revamp. Primary visuals will be prodcut pictures and case studies.
Target Market(s)
Industrial Customers in the high durability Air movement and fan/blower space; high durability enclosure and flow industries ie. mining, chamicals, manufacturing, water treatment, chemical in use manufacturing
Look and feel

```html
<!DOCTYPE html>
<html lang="en">
<head>
<meta charset="utf-8">
<title>Duraflow Composites, LLC</title>
<link rel="stylesheet" href="https://fonts.googleapis.com/css2?family=Source+Sans+3:wght@400;600;700&display=swap">
<style>
:root{
  --page-top:#f8f8f8;
  --page-bottom:#ebebeb;
  --brand:#1c2f94;
  --brand-dark:#15207a;
  --text:#555;
  --text-soft:#888;
  --text-dark:#333;
  --nav-top:#5a5a5a;
  --nav-bottom:#2e2e2e;
  --line:#e2e2e2;
  --panel:#ffffff;
  --side-bg:#ececec;
  --hero-left:#dcd8d4;
  --hero-right:#9fb6cf;
}
*{box-sizing:border-box;margin:0;padding:0}
html,body{width:1200px;height:1061px;overflow:hidden}
body{
  position:relative;
  font-family:"Source Sans 3",Arial,sans-serif;
  background:linear-gradient(var(--page-top),var(--page-bottom));
  color:var(--text);
}
.abs{position:absolute}

/* header */
.brand{left:101px;top:34px;display:flex;align-items:center;gap:14px}
.brand-square{width:40px;height:40px;background:var(--brand)}
.brand-name{font-size:27px;font-weight:600;color:var(--brand);letter-spacing:.2px}
.call{right:100px;top:24px;text-align:right}
.call-label{font-size:20px;color:#8a8a8a;line-height:26px}
.call-number{font-size:22px;font-weight:700;color:var(--text-dark);line-height:28px}

/* navigation */
.nav{left:99px;top:108px;width:1001px;height:48px;border-radius:3px 3px 0 0;
  background:linear-gradient(var(--nav-top),var(--nav-bottom));display:flex}
.nav a{color:#fff;text-decoration:none;font-size:15.5px;line-height:48px;
  padding:0 24px;border-right:1px solid #222;box-shadow:1px 0 0 #666}
.nav a.active{background:linear-gradient(#6b6b6b,#3e3e3e)}
.search{position:absolute;right:8px;top:9px;width:232px;height:29px;background:#fff;
  font-size:14px;color:#999;line-height:29px;padding-left:14px}
.search svg{position:absolute;right:10px;top:7px}

/* main panel */
.main{left:99px;top:156px;width:1001px;height:771px;background:var(--panel);
  border:1px solid #ddd;border-top:none;border-radius:0 0 4px 4px}

.hero{left:110px;top:167px;width:980px;height:311px;border-radius:3px;
  background:linear-gradient(90deg,var(--hero-left) 0%,#d9d5d1 52%,#c9c6c2 70%,var(--hero-right) 100%)}
.hero-text{left:157px;top:203px;width:390px;font-size:21px;line-height:33px;color:#555}
.hero-btn{left:157px;top:352px;width:131px;height:45px;background:#fff;border-radius:3px;
  font-size:18px;color:#555;display:flex;align-items:center;gap:9px;padding-left:14px}
.dots{left:158px;top:433px;display:flex;gap:9px}
.dots span{width:14px;height:14px;border-radius:50%;background:#8a8a8a;box-shadow:inset 0 1px 2px #555}
.dots span.on{background:#444}

.welcome{left:113px;top:520px;font-size:23px;color:var(--brand);font-weight:400}
.welcome b{font-weight:700}
.intro{left:113px;top:561px;width:695px;font-size:13.5px;line-height:25px;color:#777}
.divider{left:110px;top:663px;width:693px;height:1px;background:var(--line)}

.cats{left:110px;top:678px;width:266px}
.cats li{list-style:none;height:44px;border-bottom:1px solid #eee;font-size:16px;font-weight:700;
  color:#666;line-height:44px;position:relative}
.cats li:last-child{border-bottom:none}
.cats li.active{color:var(--brand)}
.cats li svg{position:absolute;right:-9px;top:13px}
.cats-rule{left:376px;top:673px;width:1px;height:233px;background:var(--line)}

.fan-photo{left:417px;top:683px;width:105px;height:100px;border-radius:50%;
  background:radial-gradient(#d8d8d8,#f6f6f6 70%)}
.fan-title{left:546px;top:692px;font-size:17px;font-weight:600;color:#444}
.fan-sub{left:546px;top:722px;width:255px;font-size:14px;line-height:25px;color:#888}
.fan-body{left:422px;top:797px;width:376px;font-size:14px;line-height:25px;color:#888;text-align:justify}

/* request form */
.rfi{left:835px;top:514px;width:253px;height:390px;background:var(--side-bg);border-radius:4px;overflow:hidden}
.rfi-head{height:39px;background:linear-gradient(#2a3fae,var(--brand-dark));color:#fff;
  font-size:17px;line-height:39px;padding-left:17px}
.field{position:absolute;left:10px;width:232px;height:31px;background:#fff;border-radius:3px;
  box-shadow:0 2px 2px rgba(0,0,0,.06);font-size:13px;color:#888;padding:7px 14px}
.field.tall{height:90px}
.submit{position:absolute;left:167px;top:346px;width:75px;height:30px;border-radius:3px;
  background:linear-gradient(#a4a4a4,#7c7c7c);color:#fff;font-size:14px;font-weight:700;
  text-align:center;line-height:30px}

/* footer */
.foot-nav{left:100px;top:949px;font-size:13.5px;color:#333;display:flex}
.foot-nav span{padding:0 14px;border-left:1px solid #bbb;line-height:16px}
.foot-nav span:first-child{padding-left:0;border-left:none}
.copy{left:100px;top:979px;font-size:13.5px;color:#333}
.social{left:101px;top:1012px;display:flex;gap:7px}
.social span{width:24px;height:24px;border-radius:3px;background:#4a6aa8}
.social span+span{background:#4fb3e0}
.foot-contact{right:100px;top:949px;text-align:right;font-size:13.5px;color:#333}
.foot-contact p{height:35px}
.foot-contact i{font-style:normal;color:#bbb;padding:0 12px}
</style>
</head>
<body>

<header>
  <div class="abs brand"><span class="brand-square"></span><span class="brand-name">Duraflow Composites, LLC</span></div>
  <div class="abs call"><div class="call-label">Call us</div><div class="call-number">555-014-2200</div></div>
</header>

<nav class="abs nav">
  <a class="active">Home</a><a>Products</a><a>About Us</a><a>Mission</a><a>Request Information</a><a>Contacts</a>
  <div class="search">Search
    <svg width="16" height="16" viewBox="0 0 16 16"><circle cx="6" cy="6" r="4.5" fill="none" stroke="#333" stroke-width="2.2"/><line x1="9.5" y1="9.5" x2="14" y2="14" stroke="#333" stroke-width="3" stroke-linecap="round"/></svg>
  </div>
</nav>

<div class="abs main"></div>

<section>
  <div class="abs hero" role="img" aria-label="Fibreglass fan propeller beside a rooftop air handling unit under a blue sky"></div>
  <p class="abs hero-text">We have a wide selection of fiberglass fans and other corrosion resistant air handling solutions for OEMs, Contractors and Plant Maintenance Operations.</p>
  <div class="abs hero-btn">
    <svg width="14" height="14" viewBox="0 0 14 14"><circle cx="7" cy="7" r="7" fill="#888"/><path d="M6 4l3 3-3 3" fill="none" stroke="#fff" stroke-width="1.6"/></svg>
    Contact us
  </div>
  <div class="abs dots"><span class="on"></span><span></span><span></span><span></span></div>
</section>

<section>
  <h1 class="abs welcome">Welcome to <b>Duraflow Composites</b></h1>
  <p class="abs intro">Here at Duraflow Composites, LLC., we are focused on continuous improvement of our operation. Our objective and vision is to capture more market share geographically while serving the petrochemical, military, industrial and construction markets and grow our presence in the energy industry.</p>
  <div class="abs divider"></div>

  <ul class="abs cats">
    <li class="active">Fiberglass Axial Propellers<svg width="18" height="18" viewBox="0 0 18 18"><circle cx="9" cy="9" r="8.5" fill="#f2f2f2" stroke="#ddd"/><path d="M8 6l3 3-3 3" fill="none" stroke="#666" stroke-width="1.3"/></svg></li>
    <li>Fiberglass Axial Fans<svg width="18" height="18" viewBox="0 0 18 18"><circle cx="9" cy="9" r="8.5" fill="#f2f2f2" stroke="#ddd"/><path d="M10 6l-3 3 3 3" fill="none" stroke="#999" stroke-width="1.3"/></svg></li>
    <li>Fiberglass Centrifugal Fans<svg width="18" height="18" viewBox="0 0 18 18"><circle cx="9" cy="9" r="8.5" fill="#f2f2f2" stroke="#ddd"/><path d="M10 6l-3 3 3 3" fill="none" stroke="#999" stroke-width="1.3"/></svg></li>
    <li>Fiberglass Louvers and Dampers<svg width="18" height="18" viewBox="0 0 18 18"><circle cx="9" cy="9" r="8.5" fill="#f2f2f2" stroke="#ddd"/><path d="M10 6l-3 3 3 3" fill="none" stroke="#999" stroke-width="1.3"/></svg></li>
    <li>High Plume Exhaust Fans<svg width="18" height="18" viewBox="0 0 18 18"><circle cx="9" cy="9" r="8.5" fill="#f2f2f2" stroke="#ddd"/><path d="M10 6l-3 3 3 3" fill="none" stroke="#999" stroke-width="1.3"/></svg></li>
  </ul>
  <div class="abs cats-rule"></div>

  <div class="abs fan-photo" role="img" aria-label="Grey fibreglass fan propeller"></div>
  <h2 class="abs fan-title">Fan Propellers</h2>
  <p class="abs fan-sub">Curabitur varius lorem sed diam pharetra, sit amet congue mauris commodo</p>
  <p class="abs fan-body">Donec semper, ante sit amet aliquam pulvinar, enim orci gravida tortor, nec auctor dui erat quis erat. Sed condimentum, enim ac blandit aliquam, justo mi iaculis urna, a euismod ipsum metus quis elit. Interdum et malesuada fames ac.</p>
</section>

<aside class="abs rfi">
  <div class="rfi-head">Request for Information</div>
  <div class="field" style="top:32px">Name</div>
  <div class="field" style="top:77px">Company</div>
  <div class="field" style="top:122px">Title</div>
  <div class="field" style="top:167px">E-mail</div>
  <div class="field tall" style="top:212px">Address</div>
  <div class="submit">SUBMIT</div>
</aside>

<footer>
  <div class="abs foot-nav"><span>Home</span><span>Products</span><span>About Us</span><span>Mission</span><span>Request Information</span><span>Contacts</span></div>
  <p class="abs copy">Copyright &copy; 2013 Duraflow Composites, LLC. &nbsp;All rights reserved.</p>
  <div class="abs social"><span></span><span></span></div>
  <div class="abs foot-contact">
    <p>18 Mill Road / P.O. Box 210, Harlow, NY 10990</p>
    <p>Tel: 555-014-2200<i>|</i>Fax: 555-014-2201</p>
    <p>Email : sales@duraflowcomp.com</p>
  </div>
</footer>

</body>
</html>
```